Leadership and Team Coaching Blog Template for my company, Garnet Lowell Pty Ltd

I need a consistent design I can use for publications. I am a leadership coach as well as a team coach and I also am a pretty good facilitator. I am to help people be their best both as individuals and as teams so as I enter semi-retirement I've been writing short articles to support my business. The final design should be flexible and elegant so you can tell the difference between different articles. It should also communicate confidence, energy and expertise and invite you to read further. I love blue and have attached my current logo. Not wedded to using it but clients recognise it and am sure someone clever can do something interesting with it

Target Market(s)

middle and senior leaders and Board members

Industry/Entity Type

It Company

Font styles to use
Sans Serif

Colors
0392cd
3176b5
3276b5
886aae
33b8a4
00a990
a54499
c588bc
876aae

Requirements
Must have
• flexibility to be able to re-use for different publications
Nice to have
• eye catching images
• elegant line drawing
Should not have
• clip art

```html
<!DOCTYPE html>
<html lang="en">
<head>
<meta charset="utf-8">
<title>Garnet Lowell Pty Ltd — Leadership &amp; Team Coaching</title>
<link href="https://fonts.googleapis.com/css2?family=Jost:wght@400;500&display=swap" rel="stylesheet">
<style>
:root{
  --blue:#0392cd;
  --navy:#3176b5;
  --deep:#355f8f;
  --mid:#2a8cc0;
  --sky:#55aacd;
  --teal:#33b8a4;
  --ink:#1f4a80;
  --text:#555a60;
  --muted:#8a8d92;
  --paper:#ffffff;
  --mist:#ececec;
  --night:#353038;
  --coal:#2d2a30;
  --black:#111012;
}
*{margin:0;padding:0;box-sizing:border-box}
html,body{width:1200px;height:2356px;overflow:hidden}
body{position:relative;font-family:"Jost",sans-serif;color:var(--text);background:var(--paper)}
.abs{position:absolute}
.btn-outline{position:absolute;border:1.5px solid var(--navy);color:var(--ink);font-size:12px;display:flex;align-items:center;justify-content:center;background:transparent}
.btn-light{border-color:#fff;color:#fff}

/* header */
.site-header{position:absolute;left:0;top:0;width:1200px;height:94px;background:var(--mist);border-bottom:2px solid var(--navy)}
.brand{position:absolute;left:155px;top:16px;color:var(--ink);font-size:24px;line-height:24px;font-weight:400;letter-spacing:1px}
.brand small{display:block;font-size:10px;letter-spacing:3px;line-height:16px}
.contact-mail{position:absolute;right:155px;top:10px;display:flex;align-items:center;gap:8px;font-size:15px;font-weight:500;color:var(--ink)}
.main-nav{position:absolute;left:413px;top:46px;display:flex;align-items:center;height:34px;font-size:12px;color:var(--ink)}
.main-nav .active{background:var(--blue);color:#fff;width:107px;height:34px;display:flex;align-items:center;justify-content:center;font-weight:500}
.main-nav span{margin-left:25px}
.main-nav .sep{color:#445}

/* hero */
.hero{position:absolute;left:0;top:96px;width:1200px;height:436px;background:linear-gradient(100deg,#6f7478 0%,#9a9890 30%,#b8a488 55%,#c99a62 75%,#e2b27a 100%)}
.hero h1{position:absolute;left:0;width:1200px;top:137px;text-align:center;color:#fff;font-size:29px;font-weight:400}
.hero p{position:absolute;left:0;width:1200px;top:188px;text-align:center;color:#fff;font-size:14.5px;line-height:22px}
.hero .cta{position:absolute;left:536px;top:259px;width:128px;height:33px;background:var(--blue);color:#fff;font-size:12px;display:flex;align-items:center;justify-content:center}

/* sections */
.section-title{position:absolute;left:0;width:1200px;text-align:center;color:var(--ink);font-size:24px;font-weight:400}
.about-text{position:absolute;left:251px;top:628px;width:698px;text-align:center;font-size:12px;line-height:19px;color:var(--muted)}
.publications{position:absolute;left:0;top:793px;width:1200px;height:426px;background:var(--mist)}
.pub-card{position:absolute;top:104px;width:280px;height:273px;color:#fff;text-align:center}
.pub-card svg{position:absolute;left:112px;top:22px}
.pub-card h3{position:absolute;top:92px;width:100%;font-size:17.5px;font-weight:400}
.pub-card .rule{position:absolute;left:128px;top:124px;width:24px;height:2px;background:#fff}
.pub-card p{position:absolute;left:28px;top:141px;width:224px;font-size:11.5px;line-height:17px;font-weight:500}

/* blog */
.photo{position:absolute}
.post-title{position:absolute;color:#222;font-size:19px;font-weight:400}
.meta{position:absolute;display:flex;gap:22px;font-size:11.5px;color:var(--ink)}
.meta span{display:flex;align-items:center;gap:6px}
.excerpt{position:absolute;width:370px;font-size:11.5px;line-height:18px;color:var(--muted)}

/* newsletter */
.newsletter{position:absolute;left:0;top:2018px;width:1200px;height:102px;background:var(--blue)}
.newsletter h2{position:absolute;left:155px;top:30px;color:#fff;font-size:23px;font-weight:400}
.newsletter .field{position:absolute;left:512px;top:32px;width:424px;height:38px;background:#fff;font-size:12px;color:#777;padding-left:12px;display:flex;align-items:center}
.newsletter .submit{position:absolute;left:936px;top:32px;width:107px;height:38px;background:var(--coal);color:#fff;font-size:12px;display:flex;align-items:center;justify-content:center}

/* footer */
.site-footer{position:absolute;left:0;top:2120px;width:1200px;height:194px;background:var(--night);color:#fff}
.divider{position:absolute;top:43px;width:1px;height:108px;background:#6d6870}
.foot-icon{position:absolute;top:52px}
.foot-text{position:absolute;font-size:11.5px;line-height:19px}
.social{position:absolute;top:102px;left:841px;display:flex;gap:10px}
.social i{display:block;width:24px;height:24px;border-radius:50%;background:#fff}
.copyright{position:absolute;left:0;top:2314px;width:1200px;height:42px;background:var(--black);color:#aaa;font-size:11px;display:flex;align-items:center;justify-content:center}
</style>
</head>
<body>

<header class="site-header">
  <div class="brand">GARNET<br>LOWELL<small>PTY LTD</small></div>
  <div class="contact-mail">
    <svg width="18" height="18" viewBox="0 0 18 18"><circle cx="9" cy="9" r="8" fill="none" stroke="#555" stroke-width="1.3"/><path d="M6 5.5l1.6-.5 1 2-1 .9a5 5 0 0 0 2.5 2.5l.9-1 2 1-.5 1.6c-3 .3-6.8-3.5-6.5-6.5z" fill="#555"/></svg>
    info@garnetlowell.com
  </div>
  <nav class="main-nav">
    <div class="active">Home</div>
    <span>About me</span><span class="sep">/</span>
    <span>Publications</span><span class="sep">/</span>
    <span>Blogs</span><span class="sep">/</span>
    <span>Archives</span><span class="sep">/</span>
    <span>Contact us</span>
  </nav>
</header>

<section class="hero" role="img" aria-label="Photo of a coach presenting at a whiteboard, blended with a city skyline and a seated audience in warm light">
  <h1>I Must Explain To You How All This Mistaken</h1>
  <p>except to obtain some advantage from it? But who has<br>right to find fault with a man who chooses</p>
  <div class="cta">Explore More</div>
</section>

<h2 class="section-title" style="top:571px">About Me</h2>
<p class="about-text">"On the other hand, we denounce with righteous indignation and dislike men who are so beguiled and demoralized by the charms of pleasure of the moment, so blinded by desire, that they cannot foresee the pain and trouble bound to ensue; and equal blame belongs to those who fail in their...</p>
<div class="btn-outline" style="left:551px;top:715px;width:96px;height:31px">Read More</div>

<section class="publications">
  <h2 class="section-title" style="top:40px">Publications</h2>

  <article class="pub-card" style="left:155px;background:var(--deep)">
    <svg width="56" height="48" viewBox="0 0 56 48" fill="#fff"><circle cx="28" cy="12" r="8"/><path d="M14 42c0-10 6-16 14-16s14 6 14 16z"/><circle cx="12" cy="17" r="6"/><path d="M0 40c0-8 5-12 12-12 2 0 3 .3 4 .8-3 3-4 7-4 11.2z"/><circle cx="44" cy="17" r="6"/><path d="M56 40c0-8-5-12-12-12-2 0-3 .3-4 .8 3 3 4 7 4 11.2z"/></svg>
    <h3>Publications Overview</h3><div class="rule"></div>
    <p>He rejects pleasures to secure other greater pleasures, or else he endures pains to avoid worse pains."</p>
    <div class="btn-outline btn-light" style="left:93px;top:218px;width:94px;height:31px">Read More</div>
  </article>

  <article class="pub-card" style="left:460px;background:var(--mid)">
    <svg width="56" height="48" viewBox="0 0 56 48" fill="#fff"><path d="M4 8h9v36H4zM16 8h9v36h-9zM28 8h9v36h-9z"/><path d="M40 10l10-4 4 36-10 4z"/></svg>
    <h3>Bookstore</h3><div class="rule"></div>
    <p>He rejects pleasures to secure other greater pleasures, or else he endures pains to avoid worse pains."</p>
    <div class="btn-outline btn-light" style="left:93px;top:218px;width:94px;height:31px">Read More</div>
  </article>

  <article class="pub-card" style="left:763px;background:var(--sky)">
    <svg width="56" height="48" viewBox="0 0 56 48"><path d="M10 2h30l8 8v36H10z" fill="#fff"/><path d="M14 20l30 24H14z" fill="var(--sky)" opacity=".5"/></svg>
    <h3>Magazine</h3><div class="rule"></div>
    <p>He rejects pleasures to secure other greater pleasures, or else he endures pains to avoid worse pains."</p>
    <div class="btn-outline btn-light" style="left:93px;top:218px;width:94px;height:31px">Read More</div>
  </article>
</section>

<h2 class="section-title" style="top:1261px">Our Blog</h2>

<!-- post one -->
<div class="abs" style="left:155px;top:1323px;width:54px;height:279px;background:var(--blue)"></div>
<div class="photo" style="left:209px;top:1323px;width:402px;height:279px;background:linear-gradient(180deg,#e6ecef 0%,#c9d2d6 40%,#7c6e6a 70%,#4b4144 100%)" role="img" aria-label="Photo of an audience seated in a bright seminar room facing a speaker"></div>
<div class="abs" style="left:1019px;top:1323px;width:24px;height:37px;background:var(--blue)"></div>
<h3 class="post-title" style="left:664px;top:1362px">Praesentium Voluptatum Deleniti</h3>
<div class="meta" style="left:666px;top:1418px">
  <span><svg width="11" height="11" viewBox="0 0 11 11"><rect x=".5" y="1.5" width="10" height="9" fill="none" stroke="var(--ink)"/><rect x=".5" y="1.5" width="10" height="2.5" fill="var(--ink)"/></svg>Sept. 19, 2016</span>
  <span><svg width="13" height="11" viewBox="0 0 13 11"><ellipse cx="6" cy="4.5" rx="6" ry="4" fill="var(--ink)"/><path d="M3 7l-1 3 4-2z" fill="var(--ink)"/></svg>20 Comments</span>
</div>
<p class="excerpt" style="left:666px;top:1446px">molestiae non recusandae. Itaque earum rerum hic tenetur a sapiente delectus, ut aut reiciendis voluptatibus maiores alias consequatur aut perferendis doloribus...</p>
<div class="btn-outline" style="left:666px;top:1527px;width:96px;height:31px">Read More</div>

<!-- post two -->
<div class="abs" style="left:155px;top:1627px;width:24px;height:38px;background:var(--teal)"></div>
<h3 class="post-title" style="left:177px;top:1665px">Pain Was Born And I Will Give</h3>
<div class="meta" style="left:177px;top:1721px">
  <span><svg width="11" height="11" viewBox="0 0 11 11"><rect x=".5" y="1.5" width="10" height="9" fill="none" stroke="var(--ink)"/><rect x=".5" y="1.5" width="10" height="2.5" fill="var(--ink)"/></svg>Sept. 22, 2016</span>
  <span><svg width="13" height="11" viewBox="0 0 13 11"><ellipse cx="6" cy="4.5" rx="6" ry="4" fill="var(--ink)"/><path d="M3 7l-1 3 4-2z" fill="var(--ink)"/></svg>25 Comments</span>
</div>
<p class="excerpt" style="left:177px;top:1751px">molestiae non recusandae. Itaque earum rerum hic tenetur a sapiente delectus, ut aut reiciendis voluptatibus maiores alias consequatur aut perferendis doloribus...</p>
<div class="btn-outline" style="left:177px;top:1831px;width:96px;height:32px">Read More</div>
<div class="photo" style="left:589px;top:1627px;width:404px;height:278px;background:linear-gradient(180deg,#8a5a38 0%,#b0643e 35%,#6e3b36 65%,#3a2a34 100%)" role="img" aria-label="Photo of a speaker on stage addressing a large conference audience"></div>
<div class="abs" style="left:993px;top:1627px;width:50px;height:278px;background:var(--teal)"></div>

<div class="btn-outline" style="left:537px;top:1937px;width:126px;height:31px">View All Blog</div>

<section class="newsletter">
  <h2>Sign Up Newsletter</h2>
  <div class="field">Enter Your Email</div>
  <div class="submit">Sign Up</div>
</section>

<footer class="site-footer">
  <div class="divider" style="left:360px"></div>
  <div class="divider" style="left:587px"></div>
  <div class="divider" style="left:815px"></div>

  <svg class="foot-icon" style="left:155px" width="12" height="17" viewBox="0 0 12 17"><path d="M6 0a6 6 0 0 1 6 6c0 4-6 11-6 11S0 10 0 6a6 6 0 0 1 6-6z" fill="#fff"/><circle cx="6" cy="6" r="2.2" fill="var(--night)"/></svg>
  <p class="foot-text" style="left:155px;top:94px">At vero eos et accusamus et<br>dignissimos 01234</p>

  <svg class="foot-icon" style="left:383px" width="16" height="16" viewBox="0 0 16 16"><path d="M3 1l3 .5 1 4-2 1.5a9 9 0 0 0 4 4L10.5 9l4 1 .5 3c-1 2-3 2-5 1A16 16 0 0 1 2 6C1 4 1 2 3 1z" fill="#fff"/></svg>
  <p class="foot-text" style="left:383px;top:95px;font-size:22px;line-height:28px">123-456-7890</p>

  <svg class="foot-icon" style="left:610px" width="19" height="15" viewBox="0 0 19 15"><rect width="19" height="15" rx="1.5" fill="#fff"/><path d="M1 2l8.5 6L18 2" fill="none" stroke="var(--night)" stroke-width="1.5"/></svg>
  <p class="foot-text" style="left:610px;top:94px">info@garnetlowell.com</p>

  <svg class="foot-icon" style="left:841px" width="16" height="17" viewBox="0 0 16 17" fill="#fff"><circle cx="13" cy="3" r="3"/><circle cx="3" cy="8.5" r="3"/><circle cx="13" cy="14" r="3"/><path d="M3 8.5L13 3M3 8.5L13 14" stroke="#fff" stroke-width="1.6"/></svg>
  <div class="social"><i></i><i></i><i></i><i></i><i></i></div>
</footer>

<div class="copyright">Copyright 2016. Garnet Lowell.</div>

</body>
</html>
```